Modern Venture Capital website

Design a modern website for a venture capital firm. This website should be modern and beautiful and be on par with other Venture Capital websites. I have a logo and a hero video I'd like to use. Link to hero video: https://filevault.example-share.net/file/d/9Q_7k2mzp4r8tn0W6XLfQkHa-BvvRNCT/view?usp=share_link

Preference will be given to the best design that combines design with the best images and digital content. That means no generic free stock videos 😅

I currently built a wix website to give you an idea of what content needs to be on the website. Depending on your design it can be 3 pages, or one long page. I will leave it up to you.

WEBSITE: https://marcel58274.sitebuilder-demo.net/my-site-4

Target Market(s)

Mid-career professionals, individuals interested in Venture Capital

Industry/Entity Type

Finance, venture capital, startups

Requirements
Must have
• must use the hero video I have and must use my logo. Must use high quality images that matches the website design - no generic stock images

```html
<!DOCTYPE html>
<html lang="en">
<head>
<meta charset="UTF-8">
<title>Moonlit Ventures — Venture Capital for the Late Night Hustlers</title>
<link rel="stylesheet" href="https://fonts.googleapis.com/css2?family=Outfit:wght@300;400;500;600;700&display=swap">
<style>
:root{
  --bg:#000;
  --panel:#0b0b0b;
  --panel-line:#262626;
  --orange:#ff5a0f;
  --orange-deep:#e0520a;
  --white:#fff;
  --muted:#9a9a9a;
  --soft:#c9c9c9;
}
*{margin:0;padding:0;box-sizing:border-box}
html,body{width:1200px;height:4389px;overflow:hidden;background:var(--bg)}
body{position:relative;font-family:"Outfit",sans-serif;color:var(--white)}
a{color:inherit;text-decoration:none}

/* nav */
.brand{position:absolute;left:112px;top:22px;line-height:1}
.brand-name{font-size:48px;font-weight:700;letter-spacing:-0.5px;display:block}
.brand-sub{font-size:17px;font-weight:600;letter-spacing:6px;display:block;margin-top:2px}
.nav-link{position:absolute;top:48px;font-size:14px;color:var(--white)}
.btn-outline{position:absolute;left:946px;top:38px;width:140px;height:38px;border:1.5px solid var(--orange);border-radius:20px;color:var(--orange);font-size:14px;font-weight:600;display:flex;align-items:center;justify-content:center;gap:6px}

/* hero */
.hero-media{position:absolute;left:0;top:0;width:1200px;height:740px;
  background:radial-gradient(ellipse at 50% 60%,#3a2a18 0%,#1a1410 30%,#080808 60%,#000 100%)}
.hero-lights{position:absolute;left:0;top:400px;width:1200px;height:250px;
  background:linear-gradient(180deg,rgba(0,0,0,0) 0%,rgba(120,80,40,.35) 40%,rgba(60,40,25,.2) 70%,rgba(0,0,0,0) 100%)}
.hero-title{position:absolute;left:0;width:1200px;text-align:center;font-size:56px;line-height:1}
.hero-sub{position:absolute;left:0;top:302px;width:1200px;text-align:center;font-size:23px;font-weight:400}
.btn-solid{position:absolute;background:var(--orange);border-radius:22px;color:#fff;font-weight:600;display:flex;align-items:center;justify-content:center;font-size:14px}

.vline{position:absolute;width:1.5px;background:var(--orange)}
.hline{position:absolute;height:1.5px;background:var(--orange)}
.dot{position:absolute;width:7px;height:7px;border-radius:50%;background:var(--orange)}

.section-title{position:absolute;font-size:38px;font-weight:600;white-space:nowrap}
.accent{color:var(--orange)}

.lead{position:absolute;left:140px;top:845px;width:920px;text-align:center;font-size:18px;line-height:31px;color:var(--soft)}

/* cards */
.glow-net{position:absolute;left:0;width:1200px;background:radial-gradient(ellipse at 50% 55%,rgba(120,120,120,.22) 0%,rgba(60,60,60,.1) 35%,rgba(0,0,0,0) 70%)}
.vc-card{position:absolute;top:1013px;width:248px;height:292px;border:1px solid #3a3a3a;border-radius:10px;background:linear-gradient(180deg,rgba(12,12,12,.95),rgba(20,20,20,.7));text-align:center;padding:62px 18px 0}
.vc-card h3{font-size:16px;font-weight:600;line-height:24px;margin-bottom:10px}
.vc-card p{font-size:11.5px;line-height:19px;color:var(--soft)}
.badge-ring{position:absolute;top:-44px;left:50%;margin-left:-46px;width:92px;height:92px}

/* stats */
.stat{position:absolute;width:218px;background:var(--panel);border:1px solid var(--panel-line);border-radius:6px;padding:0 0 0 31px}
.stat::before{content:"";position:absolute;left:0;top:30px;width:3px;height:44px;background:var(--orange)}
.stat b{display:block;font-size:37px;font-weight:600;margin-top:28px;line-height:1}
.stat span{display:block;font-size:17px;color:var(--muted);margin-top:8px;line-height:24px}
.body-copy{position:absolute;left:632px;width:510px;font-size:17px;line-height:26px;color:var(--soft)}

/* partners */
.hex{position:absolute;top:2215px;width:215px;height:196px}

/* better way */
.feature-media{position:absolute;left:105px;top:2825px;width:440px;height:440px;border-radius:16px;
  background:linear-gradient(160deg,#2a2020 0%,#1a1414 50%,#0c0c0c 100%)}
.feature-rail{position:absolute;left:702px;top:2840px;width:1.5px;height:330px;background:#3a2012}
.feature-icon{position:absolute;left:659px;width:86px;height:86px;border-radius:50%;border:1.5px solid var(--orange-deep);background:#000;display:flex;align-items:center;justify-content:center}
.feature-text{position:absolute;left:766px;font-size:17px;font-weight:600;line-height:24px}

/* form */
.form-panel{position:absolute;left:170px;top:3405px;width:857px;height:487px;border-radius:18px;background:linear-gradient(160deg,#e2530a 0%,#ee5d20 55%,#f06a3a 100%)}
.field{position:absolute;background:#fff;height:45px;font-size:13px;color:#333;display:flex;align-items:center;padding-left:14px;gap:6px}
.field.msg{align-items:flex-start;padding-top:14px}
.btn-dark{position:absolute;left:495px;top:3775px;width:193px;height:46px;border-radius:23px;background:#000;color:#fff;font-size:16px;font-weight:600;display:flex;align-items:center;justify-content:center}

/* footer */
.foot-h{position:absolute;top:4046px;font-size:20px;font-weight:600}
.foot-rule{position:absolute;top:4078px;width:172px;height:1px;background:#444}
.foot-list{position:absolute;top:4092px;list-style:none;font-size:14px;line-height:28px;color:var(--soft)}
.contact-row{position:absolute;left:437px;display:flex;gap:14px;font-size:14px;line-height:20px;color:var(--soft)}
.social{position:absolute;top:4140px;width:22px;height:22px;border-radius:50%;border:2px solid #fff}
.copyright{position:absolute;left:0;top:4344px;width:1200px;text-align:center;font-size:12px;color:var(--muted)}
.foot-line{position:absolute;left:0;top:4322px;width:1200px;height:1px;background:#2a2a2a}
</style>
</head>
<body>

<!-- hero -->
<div class="hero-media" role="img" aria-label="Hero video: night city skyline at dusk"></div>
<div class="hero-lights"></div>

<div class="brand"><span class="brand-name">Moonlit</span><span class="brand-sub">VENTURES</span></div>
<a class="nav-link" style="left:532px">Home</a>
<a class="nav-link" style="left:630px">Join VC</a>
<a class="nav-link" style="left:736px">Startups</a>
<a class="nav-link" style="left:851px">Login</a>
<a class="btn-outline">Get Started <svg width="11" height="11" viewBox="0 0 11 11"><path d="M2 9L9 2M4 2h5v5" stroke="#ff5a0f" stroke-width="1.6" fill="none"/></svg></a>

<h1 class="hero-title" style="top:170px;font-weight:600">Venture Capital for the</h1>
<div class="hero-title" style="top:232px;font-weight:400">Late Night Hustlers</div>
<p class="hero-sub">Become a Venture Capital Investor</p>
<a class="btn-solid" style="left:519px;top:352px;width:162px;height:40px">Learn More →</a>

<div class="vline" style="left:600px;top:660px;height:78px"></div>
<div class="dot" style="left:597px;top:735px"></div>

<!-- become a VC -->
<h2 class="section-title" style="left:481px;top:760px">Become a <span class="accent">VC</span></h2>
<p class="lead">At Moonlit Ventures, we're opening the doors to a new kind of investor, mid-career professionals and aspiring VCs who want real skin in the game, not just exposure from the sidelines.</p>

<div class="glow-net" style="top:1180px;height:300px" role="img" aria-label="Faint glowing particle network wave"></div>

<div class="vc-card" style="left:72px">
  <svg class="badge-ring" viewBox="0 0 92 92"><circle cx="46" cy="46" r="42" fill="#000"/><path d="M46 4A42 42 0 0 0 4 46A42 42 0 0 0 46 88" stroke="#ff5a0f" stroke-width="6" fill="none"/><circle cx="46" cy="46" r="34" fill="none" stroke="#ff5a0f" stroke-width="1.5"/><path d="M30 58V48M38 58V42M46 58V46M54 58V36M28 44L42 34L50 40L62 28" stroke="#fff" stroke-width="2" fill="none"/></svg>
  <h3>Hands on<br>VC Work</h3>
  <p>Each Moonlit Investor can actively be involved in sourcing, evaluating, and making key investment decisions as little or as much as they want</p>
</div>
<div class="vc-card" style="left:343px">
  <svg class="badge-ring" viewBox="0 0 92 92"><circle cx="46" cy="46" r="42" fill="#000"/><path d="M46 4A42 42 0 0 0 4 46A42 42 0 0 0 46 88" stroke="#ff5a0f" stroke-width="6" fill="none"/><circle cx="46" cy="46" r="34" fill="none" stroke="#ff5a0f" stroke-width="1.5"/><circle cx="38" cy="40" r="5" stroke="#fff" stroke-width="2" fill="none"/><circle cx="54" cy="40" r="5" stroke="#fff" stroke-width="2" fill="none"/><path d="M28 58c0-8 20-8 20 0M44 58c0-8 20-8 20 0" stroke="#fff" stroke-width="2" fill="none"/></svg>
  <h3>Earn Carry and Put<br>Your Name on<br>an Investment</h3>
  <p>Earn carry interest based on the level of your involvement on each deal.</p>
</div>
<div class="vc-card" style="left:613px">
  <svg class="badge-ring" viewBox="0 0 92 92"><circle cx="46" cy="46" r="42" fill="#000"/><path d="M46 4A42 42 0 0 0 4 46A42 42 0 0 0 46 88" stroke="#ff5a0f" stroke-width="6" fill="none"/><circle cx="46" cy="46" r="34" fill="none" stroke="#ff5a0f" stroke-width="1.5"/><rect x="32" y="34" width="28" height="22" stroke="#fff" stroke-width="2" fill="none"/><path d="M36 50L44 42L50 46L57 38" stroke="#fff" stroke-width="2" fill="none"/></svg>
  <h3>Meaningful Opportunities<br>to develop your career<br>in Venture Capital</h3>
  <p>Moonlit Investors, depending on the level of commitment and involvement, can work at our fund as Partners, Principals, Senior Associates, Associates and Venture Partners.</p>
</div>
<div class="vc-card" style="left:884px">
  <svg class="badge-ring" viewBox="0 0 92 92"><circle cx="46" cy="46" r="42" fill="#000"/><path d="M46 4A42 42 0 0 0 4 46A42 42 0 0 0 46 88" stroke="#ff5a0f" stroke-width="6" fill="none"/><circle cx="46" cy="46" r="34" fill="none" stroke="#ff5a0f" stroke-width="1.5"/><circle cx="46" cy="46" r="6" stroke="#fff" stroke-width="2" fill="none"/><circle cx="32" cy="34" r="3.5" fill="#fff"/><circle cx="60" cy="34" r="3.5" fill="#fff"/><circle cx="32" cy="58" r="3.5" fill="#fff"/><circle cx="60" cy="58" r="3.5" fill="#fff"/><path d="M35 37L41 42M57 37L51 42M35 55L41 50M57 55L51 50" stroke="#fff" stroke-width="1.6"/></svg>
  <h3>Join a community<br>of Hustlers</h3>
  <p>Network with likeminded investors, aspiring investors and limited partners.</p>
</div>

<!-- stats -->
<div class="stat" style="left:340px;top:1512px;height:135px"><b>20%</b><span>Carried Interest</span></div>
<div class="stat" style="left:107px;top:1587px;height:135px"><b>14</b><span>Pre-Seed /<br>Seed Investments</span></div>
<div class="stat" style="left:340px;top:1662px;height:135px"><b>2.5%</b><span>Management Fee</span></div>
<div class="stat" style="left:107px;top:1744px;height:136px"><b>50K</b><span>Check Size</span></div>
<div class="stat" style="left:340px;top:1814px;height:134px"><b>1M</b><span>Fund Size</span></div>

<h2 class="section-title" style="left:632px;top:1520px;font-size:38px;line-height:52px">Simplifying Success<br><span class="accent">for Founders</span></h2>
<div class="dot" style="left:1021px;top:1605px"></div>
<div class="hline" style="left:1025px;top:1608px;width:175px"></div>
<p class="body-copy" style="top:1638px">Our strength lies in our network. Our LPs and operating partners are all mid-to-senior level executives in their industries. They bring real-world corporate experience, offering strategic insights and operational support to help our portfolio companies scale efficiently.</p>
<p class="body-copy" style="top:1796px">We cut through the noise and get to the core of your business fast. If we love what you're building, we'll move. If not, we'll tell you quickly and respectfully. That lets you make</p>
<a class="btn-solid" style="left:632px;top:1908px;width:152px;height:38px">Learn More →</a>

<!-- partners -->
<div class="vline" style="left:589px;top:1950px;height:128px"></div>
<div class="dot" style="left:586px;top:2075px"></div>
<h2 class="section-title" style="left:456px;top:2095px">Our <span class="accent">Partners</span></h2>

<div class="glow-net" style="top:2300px;height:300px" role="img" aria-label="Faint glowing particle network wave"></div>
<svg class="hex" style="left:109px" viewBox="0 0 215 196" role="img" aria-label="Partner badge"><path d="M60 4H155Q166 4 172 14L210 86Q215 98 210 110L172 182Q166 192 155 192H60Q49 192 43 182L5 110Q0 98 5 86L43 14Q49 4 60 4Z" fill="#050505" stroke="#2d2d2d" stroke-width="1.5"/><rect x="60" y="88" width="95" height="20" rx="4" fill="#8a8a8a"/></svg>
<svg class="hex" style="left:358px" viewBox="0 0 215 196" role="img" aria-label="Partner badge"><path d="M60 4H155Q166 4 172 14L210 86Q215 98 210 110L172 182Q166 192 155 192H60Q49 192 43 182L5 110Q0 98 5 86L43 14Q49 4 60 4Z" fill="#050505" stroke="#2d2d2d" stroke-width="1.5"/><rect x="62" y="82" width="91" height="32" rx="4" fill="#8a8a8a"/></svg>
<svg class="hex" style="left:607px" viewBox="0 0 215 196" role="img" aria-label="Partner badge"><path d="M60 4H155Q166 4 172 14L210 86Q215 98 210 110L172 182Q166 192 155 192H60Q49 192 43 182L5 110Q0 98 5 86L43 14Q49 4 60 4Z" fill="#050505" stroke="#2d2d2d" stroke-width="1.5"/><rect x="40" y="86" width="135" height="22" rx="4" fill="#8a8a8a"/></svg>
<svg class="hex" style="left:855px" viewBox="0 0 215 196" role="img" aria-label="Partner badge"><path d="M60 4H155Q166 4 172 14L210 86Q215 98 210 110L172 182Q166 192 155 192H60Q49 192 43 182L5 110Q0 98 5 86L43 14Q49 4 60 4Z" fill="#050505" stroke="#2d2d2d" stroke-width="1.5"/><rect x="66" y="80" width="84" height="36" rx="4" fill="#8a8a8a"/></svg>

<!-- better way -->
<div class="hline" style="left:0;top:2718px;width:122px"></div>
<div class="dot" style="left:121px;top:2715px"></div>
<h2 class="section-title" style="left:150px;top:2690px;line-height:52px">A better way to be part<br>of <span class="accent">Venture Capital</span></h2>
<div class="feature-media" role="img" aria-label="Illustration of a glowing rising growth chart on a laptop"></div>

<p class="body-copy" style="left:665px;top:2708px;width:450px;font-size:17px">Backing bold founders and connecting passionate investors before the world catches on.</p>
<div class="feature-rail"></div>
<div class="feature-icon" style="top:2797px"><svg width="40" height="40" viewBox="0 0 40 40"><path d="M10 34V10H26V34M26 18H32V34M6 34H36M14 15h3M19 15h3M14 21h3M19 21h3M14 27h3M19 27h3" stroke="#fff" stroke-width="1.8" fill="none"/></svg></div>
<div class="feature-text" style="top:2816px">No previous Venture Capital<br>experience neede</div>
<div class="feature-icon" style="top:2907px"><svg width="40" height="40" viewBox="0 0 40 40"><path d="M6 34H14V26H22V18H30V10M26 6L32 6L32 12" stroke="#fff" stroke-width="1.8" fill="none"/></svg></div>
<div class="feature-text" style="top:2926px">You pick your level<br>of involvement</div>
<div class="feature-icon" style="top:3017px"><svg width="40" height="40" viewBox="0 0 40 40"><path d="M8 32L16 22L22 27L32 12M26 12H32V18M8 34H34" stroke="#fff" stroke-width="1.8" fill="none"/></svg></div>
<div class="feature-text" style="top:3036px">This isn't theory.<br>This is practice.</div>
<div class="feature-icon" style="top:3127px"><svg width="40" height="40" viewBox="0 0 40 40"><circle cx="24" cy="14" r="7" stroke="#fff" stroke-width="1.8" fill="none"/><path d="M6 30L14 26H22L28 24M6 34H30" stroke="#fff" stroke-width="1.8" fill="none"/></svg></div>
<div class="feature-text" style="top:3146px">You don't need large checks to<br>invest in Venture Capital</div>

<!-- form -->
<div class="glow-net" style="top:3700px;height:320px" role="img" aria-label="Faint glowing particle network wave"></div>
<div class="form-panel"></div>
<div class="vline" style="left:600px;top:3340px;height:108px"></div>
<div class="dot" style="left:597px;top:3444px"></div>
<h2 class="section-title" style="left:413px;top:3458px;font-size:36px">Leave Us a Message</h2>
<div class="field" style="left:272px;top:3548px;width:323px">👤 First Name</div>
<div class="field" style="left:608px;top:3548px;width:322px">👤 Last Name</div>
<div class="field" style="left:272px;top:3607px;width:323px">✉ Email address</div>
<div class="field" style="left:608px;top:3607px;width:322px">☎ Phone Number</div>
<div class="field msg" style="left:272px;top:3667px;width:656px;height:93px">💬 Message</div>
<a class="btn-dark">Send Message →</a>

<!-- footer -->
<div class="brand" style="left:120px;top:4048px"><span class="brand-name">Moonlit</span><span class="brand-sub">VENTURES</span></div>
<div class="social" style="left:127px" aria-label="Social profile"></div>
<div class="social" style="left:176px" aria-label="Social profile"></div>
<div class="social" style="left:224px" aria-label="Social profile"></div>
<div class="social" style="left:272px" aria-label="Social profile"></div>

<div class="foot-h" style="left:437px">Contact Us</div>
<div class="foot-rule" style="left:437px"></div>
<div class="contact-row" style="top:4092px"><svg width="20" height="20" viewBox="0 0 20 20"><path d="M5 2L8 6L6 8Q8 12 12 14L14 12L18 15L16 18Q8 18 2 6Z" fill="#fff"/></svg><span>555-014-2290</span></div>
<div class="contact-row" style="top:4133px"><svg width="20" height="20" viewBox="0 0 20 20"><rect x="1" y="4" width="18" height="13" rx="1" fill="#fff"/><path d="M1 5L10 12L19 5" stroke="#000" stroke-width="1.5" fill="none"/></svg><span>hello@moonlitvc.example</span></div>
<div class="contact-row" style="top:4174px"><svg width="20" height="20" viewBox="0 0 20 20"><path d="M10 1A6 6 0 0 0 4 7C4 12 10 19 10 19S16 12 16 7A6 6 0 0 0 10 1Z" fill="#fff"/><circle cx="10" cy="7" r="2" fill="#000"/></svg><span>418 Lantern Row<br>Oakridge, CA 94020</span></div>

<div class="foot-h" style="left:698px">Navigation</div>
<div class="foot-rule" style="left:698px"></div>
<ul class="foot-list" style="left:698px"><li>Solutions</li><li>Vision</li><li>Programs</li><li>Blogs</li><li>Join Us</li></ul>

<div class="foot-h" style="left:925px">Resources</div>
<div class="foot-rule" style="left:925px"></div>
<ul class="foot-list" style="left:925px"><li>Terms of Use</li><li>Privacy Policy</li><li>Sitemap</li><li>Contact</li></ul>

<div class="foot-line"></div>
<p class="copyright">Copyright © 2025 Moonlit Ventures. All Right Reserved</p>

</body>
</html>
```